Design Our Camera Package Graphic Must Be Awesome! We Have Lots More Work!

We want the attached graphic redesigned to feature our camera packages instead of the the home theater package. The information to be included in the package you can find in the second attachment. We have also included our logo. We want a really nice graphic the winner will have to make 3 graphic all with exact layout but slightly different see our website for an example http://brixtonlanefitters.example/home-theater-packages/#.VUPmopPz7zw. Remember this design will be built around the attached file named: Package Graphic info. Your design must standout. If you do really good job we will have a lot more work for you in the future. .

Target Market(s)

Home Owners

Industry/Entity Type

Camera

Font styles to use
Sans Serif

Colors
0255a3
33a6d7
85acd3
3277b5
ffffff

Requirements
Must have
• Pictures of dome cameras and bullet cameras, dvr, our company logo and MUST LOOK AWESOME!
Should not have
• We have included an example of what we are not looking for

```html
<!DOCTYPE html>
<html lang="en">
<head>
<meta charset="utf-8">
<title>Brixton Lane Fitters – Camera Packages</title>
<link rel="stylesheet" href="https://fonts.googleapis.com/css2?family=Arimo:wght@400;700&family=Open+Sans:wght@700&display=swap">
<style>
  :root {
    --frame-blue: #0b55a3;
    --band-blue: #0a4f98;
    --panel-blue: #2fa4d8;
    --divider-grey: #7d8a96;
    --ink: #0d1a26;
    --brand-brown: #4a2e1e;
    --white: #ffffff;
    --floor-light: #f1f2f4;
    --floor-grey: #d9dce1;
    --btn-top: #9fd6f4;
    --btn-mid: #3a93d6;
    --btn-bottom: #0f5aa8;
  }
  * { box-sizing: border-box; margin: 0; padding: 0; }
  html, body { width: 1200px; height: 900px; overflow: hidden; background: var(--white); }
  body { position: relative; font-family: "Arimo", Arial, sans-serif; color: var(--ink); }

  .package-card {
    position: absolute; left: 303px; top: 190px; width: 581px; height: 445px;
    background: var(--frame-blue); border-radius: 10px; overflow: hidden;
  }

  .hero {
    position: absolute; left: 4px; top: 5px; width: 573px; height: 232px;
    border-radius: 8px 8px 0 0; overflow: hidden;
    background: linear-gradient(180deg, var(--floor-grey) 0%, var(--floor-light) 55%, var(--white) 100%);
  }
  .hero-home-photo {
    position: absolute; left: 0; top: 0; width: 573px; height: 170px;
    background:
      linear-gradient(180deg, #a9c7de 0%, rgba(169,199,222,0) 35%),
      linear-gradient(90deg, #cfc58f 0%, #d6cc98 30%, #8f969c 52%, #6d7780 72%, #7a9a63 100%);
  }
  .hero-home-photo::after {
    content: ""; position: absolute; left: 0; right: 0; bottom: 0; height: 22px;
    background: linear-gradient(180deg, rgba(241,242,244,0) 0%, var(--floor-light) 100%);
  }
  .hero-camera-kit {
    position: absolute; left: 262px; top: 118px; width: 290px; height: 110px;
    border-radius: 14px 14px 4px 4px;
    background: linear-gradient(180deg, #c7cbd0 0%, #9aa0a7 45%, #4e555c 100%);
  }

  .brand-name {
    position: absolute; left: 44px; top: 182px;
    display: flex; align-items: center; gap: 6px;
    font-family: "Arimo", Arial, sans-serif; font-weight: 700;
    font-size: 12px; letter-spacing: 0.6px; text-transform: uppercase;
    color: var(--brand-brown);
  }
  .brand-name .brand-square { width: 9px; height: 9px; background: var(--brand-brown); }

  .header-band { position: absolute; left: 0; top: 237px; width: 581px; height: 16px; background: var(--band-blue); }
  .header-divider { position: absolute; left: 0; top: 253px; width: 581px; height: 4px; background: var(--divider-grey); }

  .details-panel { position: absolute; left: 0; top: 257px; width: 581px; height: 127px; background: var(--panel-blue); }
  .package { position: absolute; top: 0; font-size: 8px; line-height: 9.3px; }
  .package-left { left: 20px; }
  .package-right { left: 310px; }
  .package-title { font-weight: 700; font-size: 7.6px; text-transform: uppercase; position: absolute; white-space: nowrap; }
  .package-left .package-title { left: 26px; top: 7px; }
  .package-right .package-title { left: 19px; top: 9px; }
  .includes-label { font-weight: 700; font-size: 8.4px; position: absolute; white-space: nowrap; }
  .package-left .includes-label { left: 0; top: 25px; }
  .package-right .includes-label { left: 0; top: 28px; }
  .feature-list { position: absolute; list-style: none; white-space: nowrap; }
  .package-left .feature-list { left: 15px; top: 43px; }
  .package-right .feature-list { left: 15px; top: 48px; }
  .feature-list li { position: relative; padding-left: 7px; }
  .feature-list li::before {
    content: ""; position: absolute; left: 0; top: 3.3px;
    width: 3px; height: 3px; border-radius: 50%; background: var(--ink);
  }

  .price-band { position: absolute; left: 0; top: 384px; width: 581px; height: 61px; background: var(--frame-blue); }
  .price-button {
    position: absolute; top: 20px; width: 130px; height: 20px; border-radius: 10px;
    background: linear-gradient(180deg, var(--btn-top) 0%, var(--btn-mid) 50%, var(--btn-bottom) 52%, #2a7fc9 100%);
    box-shadow: 0 0 0 1px #0a3f7a, 0 1px 2px rgba(0,0,0,.4);
    font-family: "Open Sans", Arial, sans-serif; font-weight: 700; color: var(--white);
    font-size: 12.5px; line-height: 20px; text-align: center;
  }
  .price-button sup { font-size: 6px; vertical-align: 5px; margin-left: 1px; }
  .price-left { left: 59px; }
  .price-right { left: 352px; }
</style>
</head>
<body>
  <section class="package-card">
    <div class="hero">
      <div class="hero-home-photo" role="img" aria-label="Photo of a two-storey suburban home with stone trim, wooden gables and green trees"></div>
      <div class="hero-camera-kit" role="img" aria-label="Product photo of a security kit: four dark dome cameras, two white bullet cameras and a black DVR recorder"></div>
      <div class="brand-name"><span class="brand-square"></span>Brixton Lane Fitters</div>
    </div>

    <div class="header-band"></div>
    <div class="header-divider"></div>

    <div class="details-panel">
      <div class="package package-left">
        <h2 class="package-title">4 Camera Installation Package</h2>
        <p class="includes-label">Includes:</p>
        <ul class="feature-list">
          <li>Conduct a site survey and explain Installation</li>
          <li>Unpack Your Camera/DVR system</li>
          <li>Mount and Secure your Cameras</li>
          <li>Conceal Wiring from mount to DVR viewing room</li>
          <li>Program Basic functions on the DVR</li>
          <li>Tutorial on basic features of your new system</li>
          <li>Clean up work area and remove installation debris</li>
        </ul>
      </div>
      <div class="package package-right">
        <h2 class="package-title">4 Camera Installation with Equipment</h2>
        <p class="includes-label">Includes:</p>
        <ul class="feature-list">
          <li>Conduct a site survey and explain Installation</li>
          <li>Mount and Secure your Cameras</li>
          <li>Conceal Wiring from mount to DVR viewing room</li>
          <li>Program Basic functions on the DVR</li>
          <li>Tutorial on basic features of your new system</li>
          <li>Clean up work area and remove installation debris</li>
          <li>4 night vision/color cameras</li>
        </ul>
      </div>
    </div>

    <div class="price-band">
      <div class="price-button price-left">$399<sup>99</sup></div>
      <div class="price-button price-right">$399<sup>99</sup></div>
    </div>
  </section>
</body>
</html>
```